40-year-old commercial construction firm :: Business Card Revamp

We are a 40 year-old, private general construction company based in Dallas, Texas, and we are considering updating our business cards, which could lead to a larger "brand refresh" campaign.

We work in a competitive environment, selling to business owners and executives making large scale purchasing decisions on behalf of their firms. A majority of our business is repeat business, with a long sales-cycle; while business can be difficult to identify and land, the effort is often rewarded with multiple projects.

We are open to a logo "refresh" as well as designs that incorporate the existing logo.

Target Market(s)

B2B selling to business owners/executives/end users who make facility decisions for their firms.

Industry/Entity Type

Construction Company

Contact Information for Business Card

Refresh from the example provided

Logo Text

Harkel Building Company :: See card example

Font styles to use
Other font styles liked:
• See sample card :: Designers to choose

Colors

Designer to choose colors to be used in the design.

Requirements
Must have
• Design should convey:
• Confidence
• Competence
• Capability
• Stability
• Tagline: Genuine Relationships :: Superior Services :: Environmentally Aware
Nice to have
• A solid design that is transferable from print to online.
• Note that we are also considering a painted-edge printing / card design
Should not have
• Too much color or whimsy. Our clients tend to be the serious type, and we work hard to present a serious, professional presence in the marketplace.

```html
<!DOCTYPE html>
<html lang="en">
<head>
<meta charset="utf-8">
<title>Harkel Building Company — Business Card</title>
<link href="https://fonts.googleapis.com/css2?family=Montserrat:wght@500;600;700&display=swap" rel="stylesheet">
<style>
  :root {
    --backdrop: #c9ccca;
    --card: #1d1e20;
    --card-edge: #2a2b2e;
    --gold: #b8962e;
    --gold-soft: #a88a2e;
  }
  * { margin: 0; padding: 0; box-sizing: border-box; }
  html, body { width: 1200px; height: 800px; overflow: hidden; }
  body {
    background: var(--backdrop);
    font-family: "Montserrat", sans-serif;
    color: var(--gold);
    display: flex;
    align-items: center;
    justify-content: center;
    gap: 48px;
  }
  .card {
    position: relative;
    width: 540px;
    height: 309px;
    background: linear-gradient(135deg, var(--card-edge), var(--card) 60%);
    box-shadow: 0 10px 30px rgba(0,0,0,.25);
  }

  /* Contact side */
  .person { position: absolute; left: 70px; top: 70px; }
  .person-name { font-size: 20px; font-weight: 700; letter-spacing: 2.5px; }
  .person-role { font-size: 11px; font-weight: 500; letter-spacing: 1.6px; margin-top: 2px; padding-left: 12px; }

  .contact { position: absolute; left: 300px; top: 150px; display: flex; }
  .contact-icons { width: 22px; display: flex; flex-direction: column; align-items: center; }
  .contact-icons svg { width: 10px; height: 10px; fill: var(--gold); }
  .contact-icons .icon-phone { margin-top: 6px; }
  .contact-icons .icon-pin { margin-top: 36px; }
  .contact-rule { width: 2px; background: var(--gold); margin-right: 12px; }
  .contact-list { font-size: 10.5px; font-weight: 600; letter-spacing: 1.2px; line-height: 1.35; }
  .contact-list .label { font-weight: 700; margin-top: 14px; }
  .contact-list .plain { font-weight: 500; }

  /* Brand side */
  .brand { position: absolute; right: 52px; top: 150px; display: flex; align-items: center; gap: 14px; }
  .brand-dot { width: 44px; height: 44px; border: 5px solid var(--gold); border-radius: 50%; }
  .brand-name { font-size: 19px; font-weight: 700; letter-spacing: 2px; text-transform: uppercase; }
</style>
</head>
<body>

  <section class="card card-contact">
    <div class="person">
      <div class="person-name">DEAN CARVER</div>
      <div class="person-role">Business development</div>
    </div>
    <div class="contact">
      <div class="contact-icons">
        <svg class="icon-phone" viewBox="0 0 10 10"><path d="M2 0h2l1 2.5-1.3 1a6 6 0 0 0 2.8 2.8l1-1.3L10 6v2c0 1-1 2-2 2A8 8 0 0 1 0 2c0-1 1-2 2-2z"/></svg>
        <svg class="icon-pin" viewBox="0 0 10 10"><path d="M5 0a3.6 3.6 0 0 1 3.6 3.6C8.6 6.4 5 10 5 10S1.4 6.4 1.4 3.6A3.6 3.6 0 0 1 5 0zm0 2.2a1.4 1.4 0 1 0 0 2.8 1.4 1.4 0 0 0 0-2.8z"/></svg>
      </div>
      <div class="contact-rule"></div>
      <div class="contact-list">
        <div>214.555.0142</div>
        <div>dcarver@harkelbuild.com</div>
        <div class="label">U.S. CORPORATE OFFICE</div>
        <div class="plain">1870 Ridgemont Drive</div>
        <div class="plain">Dallas, Texas 75230</div>
        <div>972.555.0188</div>
        <div>972.555.0193</div>
        <div>harkelbuild.com</div>
      </div>
    </div>
  </section>

  <section class="card card-brand">
    <div class="brand">
      <div class="brand-dot"></div>
      <div class="brand-name">Harkel Building Company</div>
    </div>
  </section>

</body>
</html>
```